Website for a company focused on genealogical products and historical items

I need a website designed using our current branding.

R. T. Guildhouse: R. T. Guildhouse: Keepers of Rare Lineage Prints

Our company sells ancestral art, downloadable worksheets pertaining to genealogy, and we offer weekend workshops and seminars.

the website should have the following pages:
landing page
products page: to include three different products: 1. a physical product with an intake form the customer completes online, 2. a downloadable product, and 3. a lecture/presentation booking page
about us page/history
contact page/sign up page

The website will include portraits of historical figures in gold frames, lots of white background, very clean design. We would like the website to feel fresh and clean, bright.

Target Market(s)

Older Americans interested in their family heritage and lineage

Industry/Entity Type

Genealogy, research, history, lectures

Coding

Coded - Design and coding required

Number of Pages Required

5+ page

Font styles to use
Serif
Other font styles liked:
• Libre Baskerville, Aliey, one historical script - P22 Royalist

Colors
0094D4
00A9DD
6FCCEA
C7EBF8
E9F6FB

Requirements
Must have
• must have our color branding and logo (pdf attached, and I can send original files), simple design, not too many images on each page (maybe one image per page)
Nice to have
• Nice to have clean design, all pages the same "look"
Should not have
• no black backgrounds, nothing too busy

```html
<!DOCTYPE html>
<html lang="en">
<head>
<meta charset="utf-8">
<title>R. T. Guildhouse – Keepers of Rare Lineage Prints</title>
<link rel="stylesheet" href="https://fonts.googleapis.com/css2?family=Young+Serif&family=Libre+Baskerville:ital@1&family=Poppins:wght@400;500;600&display=swap">
<style>
:root{
  --brown:#4f3422;
  --brown-mid:#6b4429;
  --sage:#9ab7a6;
  --gray:#f2f2f2;
  --cream:#fdf5e7;
  --text:#3a3a3a;
  --white:#ffffff;
  --gold-a:#f0cf6e;
  --gold-b:#b07d26;
  --gold-c:#8a5a16;
}
*{box-sizing:border-box;margin:0;padding:0}
html,body{width:1200px;height:3172px;overflow:hidden;background:var(--white)}
body{position:relative;font-family:'Poppins',sans-serif;color:var(--text)}
.abs{position:absolute}
.display{font-family:'Young Serif',serif;color:var(--brown);text-transform:uppercase;line-height:1;white-space:nowrap}
.script{font-family:'Libre Baskerville',serif;font-style:italic;color:var(--brown)}
.body-text{font-size:14px;line-height:26.5px;color:#333}
.btn{position:absolute;display:flex;align-items:center;justify-content:center;font-family:'Poppins',sans-serif;font-weight:600;font-size:15px;letter-spacing:.6px;text-transform:uppercase;color:var(--white);background:var(--sage);text-decoration:none;white-space:nowrap}
.btn.dark{background:var(--brown)}

/* photographs */
.photo{position:absolute;overflow:hidden}
.photo::after{content:"";position:absolute;inset:0;background:radial-gradient(ellipse at center,rgba(255,255,255,0) 45%,rgba(0,0,0,.28) 100%)}
.print{position:absolute;background:#fff;padding:10px;box-shadow:0 8px 20px rgba(0,0,0,.25)}
.print .photo{position:relative;width:100%;height:100%}

/* gilded frames */
.gilt{position:absolute;padding:20px;background:
  linear-gradient(135deg,var(--gold-a),var(--gold-b) 25%,var(--gold-a) 50%,var(--gold-c) 75%,var(--gold-a));
  box-shadow:inset 0 0 0 2px var(--gold-c),inset 0 0 0 6px rgba(255,235,170,.6),inset 0 0 0 9px var(--gold-b),0 3px 8px rgba(0,0,0,.18)}
.gilt .photo{position:relative;width:100%;height:100%;box-shadow:0 0 0 3px var(--gold-c),0 0 0 5px #f3d98a}

/* header */
.site-header{position:absolute;left:0;top:0;width:1200px;height:119px;background:var(--white)}
.brand-badge{position:absolute;left:74px;top:0;width:181px;height:277px;background:var(--white);border-radius:0 0 90px 90px;display:flex;flex-direction:column;align-items:center;justify-content:center;z-index:3;padding-top:10px}
.brand-mark{width:20px;height:20px;background:var(--sage);border-radius:50%;margin-bottom:14px}
.brand-name{font-family:'Young Serif',serif;color:var(--brown);font-size:27px;line-height:1.1;text-align:center;text-transform:uppercase}
.nav a{position:absolute;top:54px;font-size:15px;font-weight:600;color:var(--brown);text-decoration:none;white-space:nowrap}
.nav a.active{text-decoration:underline;text-underline-offset:5px}
.nav .btn{top:38px;height:49px;font-size:14px}

/* hero */
.hero{position:absolute;left:0;top:119px;width:1200px;height:615px;background:var(--gray);overflow:hidden}

/* products */
.products{position:absolute;left:0;top:1238px;width:1200px;height:575px;background:var(--cream)}
.card-title{position:absolute;font-size:17px;font-weight:600;color:var(--brown-mid);white-space:nowrap}
.card-desc{position:absolute;font-size:13px;line-height:19px;color:#333;width:215px}
.price{position:absolute;font-size:17px;font-weight:600;color:#222}
.cart{width:111px;height:39px;font-size:13px;text-transform:none;letter-spacing:.2px}
.arrow{position:absolute;top:1640px}

/* footer */
.site-footer{position:absolute;left:0;top:2784px;width:1200px;height:388px;background:var(--gray)}
.foot-h{position:absolute;font-size:19px;font-weight:600;color:var(--brown);white-space:nowrap}
.foot-link{position:absolute;font-size:12.5px;color:#333;white-space:nowrap}
.foot-icon{position:absolute}
.social{position:absolute}
</style>
</head>
<body>

<header class="site-header">
  <div class="brand-badge">
    <span class="brand-mark"></span>
    <span class="brand-name">R. T.<br>Guildhouse</span>
  </div>
  <nav class="nav">
    <a href="#" class="active" style="left:439px">Home</a>
    <a href="#" style="left:529px">About Us</a>
    <a href="#" style="left:642px">Products</a>
    <a href="#" style="left:756px">Contact Us</a>
    <a href="#" class="btn" style="left:873px;width:121px">Booking</a>
    <a href="#" class="btn" style="left:1004px;width:122px">Download</a>
  </nav>
</header>

<section class="hero">
  <h1 class="display abs" style="left:79px;top:238px;font-size:39px">R. T. Guildhouse</h1>
  <p class="script abs" style="left:79px;top:292px;font-size:33px;line-height:43px;width:420px">Keepers of Rare<br>Lineage Prints</p>
  <a href="#" class="btn" style="left:79px;top:394px;width:163px;height:49px">View Products</a>
  <a href="#" class="btn dark" style="left:257px;top:394px;width:137px;height:49px">Read More</a>

  <div class="print" style="left:757px;top:70px;width:395px;height:470px;transform:rotate(4deg)">
    <div class="photo" role="img" aria-label="Sepia photograph of an antique oil lantern"
         style="background:radial-gradient(ellipse at 62% 55%,#a58a72 0%,#5e4536 35%,#2d2019 70%),linear-gradient(150deg,#7b6252,#3a2a22)"></div>
  </div>
  <div class="print" style="left:532px;top:160px;width:355px;height:390px;transform:rotate(-5deg)">
    <div class="photo" role="img" aria-label="Aged sepia family portrait photograph"
         style="background:radial-gradient(ellipse at 50% 60%,#a89673 0%,#857454 45%,#c1b08c 100%),linear-gradient(160deg,#c7b897,#8b7b5c)"></div>
  </div>
</section>

<section class="about">
  <div class="gilt" style="left:74px;top:807px;width:513px;height:354px;padding:46px">
    <div class="photo" style="background:#fff;display:flex;flex-direction:column;align-items:center;justify-content:center">
      <span class="brand-mark" style="width:26px;height:26px"></span>
      <span class="brand-name" style="font-size:34px">R. T. Guildhouse</span>
    </div>
  </div>
  <h2 class="display abs" style="left:616px;top:817px;font-size:35px">About R. T. Guildhouse</h2>
  <p class="script abs" style="left:616px;top:865px;font-size:29px;white-space:nowrap">Keepers of Rare Lineage Prints</p>
  <p class="body-text abs" style="left:616px;top:916px;width:500px">Sed ut perspiciatis unde omnis iste natus error sit voluptatem accusantium doloremque laudantium, totam rem aperiam, eaque ipsa quae ab illo inventore veritatis et quasi architecto beatae vitae dicta sunt explicabo. Nemo enim ipsam voluptatem quia voluptas sit aspernatur aut odit aut fugit, sed quia consequuntur magni dolores eos qui ratione voluptatem sequi nesciunt.</p>
  <a href="#" class="btn" style="left:616px;top:1100px;width:151px;height:50px">Read More</a>
</section>

<section class="products">
  <h2 class="display abs" style="left:75px;top:133px;font-size:40px;line-height:43px">Our<br>Products</h2>
  <p class="body-text abs" style="left:76px;top:226px;width:320px">Sed ut perspiciatis unde omnis iste natus error sit voluptatem&nbsp; accusantium doloremque laudantium, totam rem aperiam, eaque ipsa quae ab illo inventore veritatis et quasi arch tecto beatae vitae dicta.</p>
  <a href="#" class="btn" style="left:76px;top:389px;width:152px;height:49px">View All</a>
</section>
<svg class="arrow" style="left:264px" width="16" height="26" viewBox="0 0 16 26"><path d="M13 2 3 13l10 11" fill="none" stroke="#333" stroke-width="2"/></svg>
<svg class="arrow" style="left:306px" width="16" height="26" viewBox="0 0 16 26"><path d="M3 2l10 11L3 24" fill="none" stroke="#333" stroke-width="2"/></svg>

<div class="gilt" style="left:433px;top:1301px;width:225px;height:324px;padding:28px">
  <div class="photo" role="img" aria-label="Carved tribal mask artwork" style="background:radial-gradient(ellipse at 50% 50%,#4a3d30 0%,#6f6659 35%,#c9cccd 75%,#e6e8e9 100%)"></div>
</div>
<div class="gilt" style="left:690px;top:1301px;width:224px;height:324px;padding:28px">
  <div class="photo" role="img" aria-label="Modern abstract portrait artwork" style="background:radial-gradient(ellipse at 45% 55%,#c98e5a 0%,#8a6b45 30%,#3b3a35 65%,#2a2a2a 100%)"></div>
</div>
<div class="gilt" style="left:946px;top:1301px;width:224px;height:324px;padding:28px">
  <div class="photo" role="img" aria-label="Sepia antique portrait of a young woman" style="background:radial-gradient(ellipse at 50% 40%,#c9b58c 0%,#a8916a 40%,#4a3b2b 100%)"></div>
</div>

<div class="card-title" style="left:433px;top:1640px">Product Heading</div>
<div class="card-desc" style="left:433px;top:1666px">Sed ut perspiciatis unde omnis iste natus</div>
<div class="price" style="left:432px;top:1718px">$210.00</div>
<a href="#" class="btn cart" style="left:513px;top:1711px">Add to Cart</a>

<div class="card-title" style="left:690px;top:1640px">Product Heading</div>
<div class="card-desc" style="left:690px;top:1666px">Sed ut perspiciatis unde omnis iste natus</div>
<div class="price" style="left:690px;top:1718px">$210.00</div>
<a href="#" class="btn cart" style="left:771px;top:1711px">Add to Cart</a>

<div class="card-title" style="left:946px;top:1640px">Product Heading</div>
<div class="card-desc" style="left:946px;top:1666px">Sed ut perspiciatis unde omnis iste natus</div>
<div class="price" style="left:945px;top:1718px">$210.00</div>
<a href="#" class="btn cart" style="left:1026px;top:1711px">Add to Cart</a>

<section class="worksheets">
  <div class="photo" role="img" aria-label="Scattered vintage photographs over an old handwritten certificate"
       style="left:74px;top:1881px;width:513px;height:383px;background:radial-gradient(ellipse at 75% 30%,#6d665d 0%,#3b3631 40%,rgba(59,54,49,0) 70%),linear-gradient(135deg,#ece6da 0%,#d8cfbf 35%,#8d8377 60%,#2e2a26 85%,#cfc8bc 100%)"></div>
  <h2 class="display abs" style="left:616px;top:1953px;font-size:40px">Worksheets</h2>
  <p class="body-text abs" style="left:616px;top:2012px;width:500px">Sed ut perspiciatis unde omnis iste natus error sit voluptatem accusantium doloremque laudantium, totam rem aperiam, eaque ipsa quae ab illo inventore veritatis et quasi architecto beatae vitae dicta sunt explicabo.</p>
  <a href="#" class="btn" style="left:616px;top:2139px;width:151px;height:49px">Download</a>
</section>

<section class="lecture">
  <h2 class="display abs" style="left:76px;top:2395px;font-size:40px">Lecture</h2>
  <p class="body-text abs" style="left:76px;top:2450px;width:500px">Sed ut perspiciatis unde omnis iste natus error sit voluptatem accusantium doloremque laudantium, totam rem aperiam, eaque ipsa quae ab illo inventore veritatis et quasi architecto beatae vitae dicta sunt explicabo.</p>
  <a href="#" class="btn" style="left:76px;top:2577px;width:152px;height:49px">Book Now</a>
  <div class="photo" role="img" aria-label="Presenter giving a lecture at a flip chart to seated attendees"
       style="left:617px;top:2320px;width:513px;height:384px;background:radial-gradient(ellipse at 55% 35%,#5d7fa8 0%,rgba(93,127,168,0) 22%),radial-gradient(ellipse at 85% 80%,#c9857a 0%,rgba(201,133,122,0) 30%),linear-gradient(180deg,#eeebe4 0%,#d9d4c8 45%,#9b7a5e 75%,#6e5442 100%)"></div>
</section>

<footer class="site-footer">
  <div class="abs" style="left:74px;top:70px;width:160px;display:flex;flex-direction:column;align-items:center">
    <span class="brand-mark"></span>
    <span class="brand-name" style="font-size:25px">R. T.<br>Guildhouse</span>
  </div>
  <p class="foot-link" style="left:74px;top:285px;line-height:22px">© 2024 R. T. Guildhouse<br>All Rights Reserved&nbsp; Privacy Policy<br>Terms &amp; Conditions</p>

  <h3 class="foot-h" style="left:343px;top:63px">Quick Links</h3>
  <a class="foot-link" style="left:343px;top:100px">Home</a>
  <a class="foot-link" style="left:343px;top:132px">About Us</a>
  <a class="foot-link" style="left:343px;top:165px">Products</a>
  <a class="foot-link" style="left:343px;top:198px">Contact Us</a>

  <h3 class="foot-h" style="left:551px;top:63px">Contact Us</h3>
  <svg class="foot-icon" style="left:551px;top:106px" width="14" height="12" viewBox="0 0 14 12"><path d="M0 2l4-2 5 2 5-2v10l-5 2-5-2-4 2z" fill="#9ab7a6"/></svg>
  <p class="foot-link" style="left:580px;top:103px;line-height:22px">48 Ledger Row Suite 12,<br>Boston 02108, United States</p>
  <svg class="foot-icon" style="left:551px;top:156px" width="13" height="13" viewBox="0 0 24 24"><path d="M6.6 10.8a15 15 0 0 0 6.6 6.6l2.2-2.2c.3-.3.7-.4 1-.2 1.1.4 2.3.6 3.6.6.6 0 1 .4 1 1V20c0 .6-.4 1-1 1C10.6 21 3 13.4 3 4c0-.6.4-1 1-1h3.5c.6 0 1 .4 1 1 0 1.3.2 2.5.6 3.6.1.3 0 .7-.2 1z" fill="#9ab7a6"/></svg>
  <p class="foot-link" style="left:580px;top:155px">+1-617-555-0148</p>
  <svg class="foot-icon" style="left:551px;top:190px" width="14" height="10" viewBox="0 0 14 10"><rect width="14" height="10" fill="#9ab7a6"/><path d="M0 0l7 5 7-5" fill="none" stroke="#f2f2f2" stroke-width="1.2"/></svg>
  <p class="foot-link" style="left:580px;top:187px">hello@rtguildhouse.com</p>
  <svg class="foot-icon" style="left:551px;top:232px" width="10" height="14" viewBox="0 0 10 14"><path d="M5 0a5 5 0 0 0-5 5c0 4 5 9 5 9s5-5 5-9a5 5 0 0 0-5-5z" fill="#4f3422"/><circle cx="5" cy="5" r="1.8" fill="#f2f2f2"/></svg>
  <p class="foot-link" style="left:580px;top:231px">Map Directions</p>

  <h3 class="foot-h" style="left:827px;top:63px">Newsletter Sign Up</h3>
  <p class="foot-link" style="left:827px;top:100px;width:300px;line-height:21px;white-space:normal">Nemo enim ipsam voluptatem quia voluptas sit aspernatur</p>
  <div class="abs" style="left:827px;top:153px;width:299px;height:45px;background:#fff;border:1px solid #ccc;display:flex;align-items:center;justify-content:space-between;padding:0 12px">
    <span style="font-size:12.5px;color:#555">Enter Email Address</span>
    <svg width="14" height="12" viewBox="0 0 14 12"><path d="M0 6h12M7 1l5 5-5 5" fill="none" stroke="#222" stroke-width="1.8"/></svg>
  </div>
  <h3 class="foot-h" style="left:827px;top:225px">Follow Us</h3>
  <svg class="social" role="img" aria-label="Social network link" style="left:827px;top:268px" width="20" height="20"><circle cx="10" cy="10" r="9" fill="none" stroke="#8a6d55" stroke-width="2"/></svg>
  <svg class="social" role="img" aria-label="Social network link" style="left:862px;top:268px" width="20" height="20"><circle cx="10" cy="10" r="9" fill="none" stroke="#8a6d55" stroke-width="2"/></svg>
  <svg class="social" role="img" aria-label="Social network link" style="left:897px;top:268px" width="20" height="20"><circle cx="10" cy="10" r="9" fill="none" stroke="#8a6d55" stroke-width="2"/></svg>
  <svg class="social" role="img" aria-label="Social network link" style="left:932px;top:268px" width="20" height="20"><circle cx="10" cy="10" r="9" fill="none" stroke="#8a6d55" stroke-width="2"/></svg>
  <svg class="social" role="img" aria-label="Social network link" style="left:967px;top:268px" width="20" height="20"><circle cx="10" cy="10" r="9" fill="none" stroke="#8a6d55" stroke-width="2"/></svg>
</footer>

</body>
</html>
```